Web Design Project

We are re-starting this project.

This project is for a totally new look and design of a website for Wablor. www.wablor-demo.net.

Wablor is a naming protocol for physical locations and can be used for fixed and mobile people, places and things. Find your friends, or find a business. Because Wablor locations point to precise geo-physical (GPS) co-ordinates, navigation to a location becomes totally reliable.
Updates

Please see the modified brief for this project

Target Market(s)

Every person and every business can have multiple !Wabs (Wablor locations), so the website needs to be appealing and fun, but easy to use and functional

Industry/Entity Type

Business

Colors
34a6d7

Requirements
Must have
• Uniqueness!

```html
<!DOCTYPE html>
<html lang="en">
<head>
<meta charset="utf-8">
<title>Wablor – Save and manage your important personal locations</title>
<link rel="stylesheet" href="https://fonts.googleapis.com/css2?family=Open+Sans:wght@400;600;700&family=Bebas+Neue&display=swap">
<style>
:root{
  --brand:#34a6d7;
  --band:#1f95d5;
  --accent:#e2451c;
  --text:#555555;
  --muted:#666666;
  --grey-band:#959595;
  --btn:#626262;
  --pin:#8e8e8e;
  --white:#ffffff;
}
*{margin:0;padding:0;box-sizing:border-box}
html,body{width:901px;height:1200px;overflow:hidden;background:var(--white)}
body{font-family:"Open Sans",Arial,sans-serif;color:var(--text);position:relative}

.site-header{position:absolute;left:0;top:0;width:901px;height:98px}
.brand{position:absolute;left:88px;top:26px;display:flex;align-items:center;gap:8px}
.brand-dot{width:18px;height:18px;border-radius:50%;background:var(--brand)}
.brand-name{font-weight:700;font-size:34px;color:var(--brand);line-height:1}
.top-nav{position:absolute;right:113px;top:46px;display:flex;gap:14px}
.top-nav a{font-size:11px;color:var(--accent);text-decoration:none;text-transform:uppercase}

.hero{position:absolute;left:0;top:98px;width:901px;height:380px;
  background:linear-gradient(180deg,#b9cfe2 0%,#c8b4a4 22%,#b98a6a 50%,#c77a54 78%,#b9623e 100%)}
.hero-caption{position:absolute;left:82px;top:314px;width:736px;height:66px;background:rgba(255,255,255,.9)}
.hero-arrow{position:absolute;top:20px;width:26px;height:26px}
.hero-arrow.prev{left:16px}
.hero-arrow.next{right:17px}
.hero-title{position:absolute;left:70px;top:10px;font-size:18.5px;font-weight:700;color:var(--brand)}
.hero-sub{position:absolute;left:70px;top:37px;font-size:10px;color:var(--muted)}

.finder{position:absolute;left:0;top:478px;width:901px;height:144px;background:var(--band)}
.finder-col{position:absolute;top:22px;width:344px}
.finder-col.who{left:82px}
.finder-col.what{left:474px}
.finder-head{display:flex;align-items:center;gap:8px;height:40px;color:var(--white);font-size:23px;white-space:nowrap}
.finder-input{margin-top:10px;height:33px;background:var(--white);display:flex;align-items:center;justify-content:space-between;padding:0 10px 0 14px}
.finder-input span{font-family:Arial,sans-serif;font-size:10.5px;color:#444}

.activity{position:absolute;left:0;top:622px;width:901px;height:381px}
.activity-item{position:absolute;display:flex;align-items:center;gap:14px}
.pin{width:50px;height:62px;position:relative;flex:none}
.pin svg{position:absolute;left:0;top:0}
.avatar{position:absolute;left:7px;top:6px;width:36px;height:36px;border-radius:50%;
  background:linear-gradient(160deg,#7a5a4c,#c99b86)}
.activity-text{font-size:14px;line-height:17px;color:var(--text);margin-top:6px}
.handle{color:var(--brand)}
.place{color:var(--accent)}

.join{position:absolute;left:0;top:1003px;width:901px;height:149px;background:var(--grey-band);text-align:center}
.join p{position:absolute;left:0;width:100%;top:31px;color:var(--white);font-size:13.5px}
.join-btn{position:absolute;left:348px;top:66px;width:204px;height:48px;background:var(--btn);color:var(--white);
  font-family:"Bebas Neue",Impact,sans-serif;font-size:40px;line-height:50px;text-decoration:none}

.site-footer{position:absolute;left:0;top:1152px;width:901px;height:48px;background:var(--band)}
.footer-links{position:absolute;left:88px;top:17px;display:flex;gap:10px}
.footer-links a{color:var(--white);font-size:10.5px;text-decoration:none}
.powered{position:absolute;left:676px;top:13px;display:flex;align-items:center;gap:8px;color:var(--white);font-size:10.5px}
.powered strong{font-size:15px;font-weight:700}
</style>
</head>
<body>

<header class="site-header">
  <div class="brand"><span class="brand-dot"></span><span class="brand-name">Wablor</span></div>
  <nav class="top-nav"><a href="#">Sign up</a><a href="#">Login</a></nav>
</header>

<section class="hero" role="img" aria-label="Photo of a hiker with an orange backpack sitting on a canyon rim, looking at a tablet map">
  <div class="hero-caption">
    <svg class="hero-arrow prev" viewBox="0 0 26 26"><circle cx="13" cy="13" r="11.5" fill="none" stroke="#34a6d7" stroke-width="2"/><path d="M15 7.5 9.5 13 15 18.5" fill="none" stroke="#34a6d7" stroke-width="2.4"/></svg>
    <div class="hero-title">Save and manage your important personal locations.</div>
    <div class="hero-sub">Home, work, favourite fishing or camping spot or any physical location on earth!&nbsp; Wablor is your address for life.</div>
    <svg class="hero-arrow next" viewBox="0 0 26 26"><circle cx="13" cy="13" r="11.5" fill="none" stroke="#34a6d7" stroke-width="2"/><path d="M11 7.5 16.5 13 11 18.5" fill="none" stroke="#34a6d7" stroke-width="2.4"/></svg>
  </div>
</section>

<section class="finder">
  <div class="finder-col who">
    <div class="finder-head">
      <svg width="32" height="30" viewBox="0 0 32 30" fill="#fff"><circle cx="11" cy="9" r="6"/><path d="M0 30c0-8 5-13 11-13s11 5 11 13z"/><path d="M25 0a6 6 0 0 0-6 6c0 4 6 10 6 10s6-6 6-10a6 6 0 0 0-6-6zm0 8.5a2.5 2.5 0 1 1 0-5 2.5 2.5 0 0 1 0 5z"/></svg>
      <span>Who would you like to find?</span>
    </div>
    <div class="finder-input"><span>enter !wab ...</span>
      <svg width="20" height="20" viewBox="0 0 20 20"><circle cx="8" cy="8" r="6" fill="none" stroke="#333" stroke-width="2.6"/><path d="M12.5 12.5 18 18" stroke="#333" stroke-width="3" stroke-linecap="round"/></svg></div>
  </div>
  <div class="finder-col what">
    <div class="finder-head">
      <svg width="38" height="38" viewBox="0 0 38 38" fill="none" stroke="#fff" stroke-width="2.4"><path d="M19 2a8 8 0 0 0-8 8c0 6 8 14 8 14s8-8 8-14a8 8 0 0 0-8-8z" fill="#fff"/><circle cx="19" cy="10" r="3" fill="#1f95d5" stroke="none"/><path d="M9 24 2 34l10-3 9 4 15-5-5-7"/><path d="M12 31l8-6 6 5"/></svg>
      <span>What would you like to find?</span>
    </div>
    <div class="finder-input"><span>enter name...</span>
      <svg width="20" height="20" viewBox="0 0 20 20"><circle cx="8" cy="8" r="6" fill="none" stroke="#333" stroke-width="2.6"/><path d="M12.5 12.5 18 18" stroke="#333" stroke-width="3" stroke-linecap="round"/></svg></div>
  </div>
</section>

<section class="activity">
  <div class="activity-item" style="left:90px;top:39px">
    <div class="pin"><svg width="50" height="62" viewBox="0 0 50 62"><path d="M25 1a24 24 0 0 0-24 24c0 11 9 19 24 36 15-17 24-25 24-36A24 24 0 0 0 25 1z" fill="#8e8e8e"/></svg><div class="avatar" role="img" aria-label="Profile photo"></div></div>
    <p class="activity-text"><span class="handle">!tessmira</span> updated their current location<br><span class="place">!tessmira.now</span> 7 hours ago</p>
  </div>
  <div class="activity-item" style="left:474px;top:39px">
    <div class="pin"><svg width="50" height="62" viewBox="0 0 50 62"><path d="M25 1a24 24 0 0 0-24 24c0 11 9 19 24 36 15-17 24-25 24-36A24 24 0 0 0 25 1z" fill="#8e8e8e"/></svg><div class="avatar" role="img" aria-label="Profile photo"></div></div>
    <p class="activity-text"><span class="handle">!julesharbor</span> updated their current location<br><span class="place">!julesharbor.now</span> 12 hours ago</p>
  </div>
  <div class="activity-item" style="left:90px;top:138px">
    <div class="pin"><svg width="50" height="62" viewBox="0 0 50 62"><path d="M25 1a24 24 0 0 0-24 24c0 11 9 19 24 36 15-17 24-25 24-36A24 24 0 0 0 25 1z" fill="#8e8e8e"/></svg><div class="avatar" role="img" aria-label="Profile photo"></div></div>
    <p class="activity-text"><span class="handle">!owenpike</span> updated their current location<br><span class="place">!owenpike.now</span> 14 hours ago</p>
  </div>
  <div class="activity-item" style="left:474px;top:138px">
    <div class="pin"><svg width="50" height="62" viewBox="0 0 50 62"><path d="M25 1a24 24 0 0 0-24 24c0 11 9 19 24 36 15-17 24-25 24-36A24 24 0 0 0 25 1z" fill="#8e8e8e"/></svg><div class="avatar" role="img" aria-label="Profile photo"></div></div>
    <p class="activity-text"><span class="handle">!corvel88</span> added a location<br><span class="place">!corvel88.home</span> 15 hours ago</p>
  </div>
  <div class="activity-item" style="left:90px;top:238px">
    <div class="pin"><svg width="50" height="62" viewBox="0 0 50 62"><path d="M25 1a24 24 0 0 0-24 24c0 11 9 19 24 36 15-17 24-25 24-36A24 24 0 0 0 25 1z" fill="#8e8e8e"/></svg><div class="avatar" role="img" aria-label="Profile photo"></div></div>
    <p class="activity-text"><span class="handle">!tessmira</span> updated their current location<br><span class="place">!tessmira.now</span> 7 hours ago</p>
  </div>
  <div class="activity-item" style="left:474px;top:238px">
    <div class="pin"><svg width="50" height="62" viewBox="0 0 50 62"><path d="M25 1a24 24 0 0 0-24 24c0 11 9 19 24 36 15-17 24-25 24-36A24 24 0 0 0 25 1z" fill="#8e8e8e"/></svg><div class="avatar" role="img" aria-label="Profile photo"></div></div>
    <p class="activity-text"><span class="handle">!julesharbor</span> updated their current location<br><span class="place">!julesharbor.now</span> 12 hours ago</p>
  </div>
</section>

<section class="join">
  <p>Lorem ipsum dolor sit amet, consectetur adipisicing elit, sed do eiusmod tempor incidore magna aliqua.</p>
  <a class="join-btn" href="#">JOIN NOW</a>
</section>

<footer class="site-footer">
  <nav class="footer-links"><a href="#">About</a><a href="#">Help</a><a href="#">Contact</a><a href="#">Privacy</a><a href="#">Terms</a><a href="#">Refunds</a><a href="#">Faq</a></nav>
  <div class="powered"><span>Powered by</span><strong>Wablor</strong></div>
</footer>

</body>
</html>
```